Lunora Vaginal Suppositories eCommerce Website Design

We are designing an ecommerce website for a new company and product. The product is vaginal moisturizer suppositories. We are going to develop this site on Shopify so you can add in any featured you have knowledge of in Shopify.

We are purposefully not adding any images to allow you to create something with your style. A similar product is petalkind.example. We would like a site similar to this in style, but obviously different not to look the same. It is a product for women so it needs to be a very feminine theme. We have had designers use thier own illustrations in previous designs that looked great, or stock images that don't look "stock" would be good. We would like the product section to look like a normal product section on Shopify, specified in the link below. The rest of the site with the featues and benefits and ingredients can be displayed creatively with images, illustrations, or product placement interspersed. Use any high quality images you have access to and we will purchase if necessary.

Use icons and symbols to represent the different benefits and ingredients.

Pay no attention to colors in the wireframe. The only defitinte color is the logo.

I put a picture of the actual suppositories so we would like to intersperse that (an individual one, not inside the package) in a few places. You can use it in the directions section for sure.

Video about wireframe: https://files.example-share.net/d/Xq82mLp0Tz/view

https://slides.example-share.net/p/Rk47vNw2Hc/edit

Target Market(s)

Women

Industry/Entity Type

Healthcare

Number of Pages Required

1 page

Requirements
Must have
• I added a "wireframe" in the description
Nice to have
Should not have

```html
<!DOCTYPE html>
<html lang="en">
<head>
<meta charset="utf-8">
<title>Lunora Vaginal Suppositories</title>
<link rel="stylesheet" href="https://fonts.googleapis.com/css2?family=Jost:wght@300;400;500;600&family=Questrial&display=swap">
<style>
  :root {
    --ink: #231f20;
    --ink-soft: #4a4244;
    --brand: #e0218a;
    --announce: #f3c8ca;
    --page: #ffffff;
    --rule: #e7e2e2;
    --blush: #f6dcdd;
    --blush-light: #fcf0f0;
    --blush-mid: #f7e2e2;
    --blush-deep: #f2c3c4;
    --btn: #2a2224;
  }
  * { box-sizing: border-box; margin: 0; padding: 0; }
  html, body { width: 960px; height: 1200px; overflow: hidden; background: var(--page); }
  body { position: relative; font-family: "Jost", sans-serif; color: var(--ink); }

  .announcement {
    position: absolute; left: 0; top: 0; width: 960px; height: 30px;
    background: var(--announce);
    display: flex; align-items: center; justify-content: center;
    font-size: 12px; font-weight: 500; letter-spacing: 0.4px;
  }
  .announcement .social { position: absolute; right: 12px; display: flex; gap: 8px; }
  .announcement .social span { width: 9px; height: 9px; border-radius: 50%; border: 1.5px solid var(--ink); display: block; }

  .site-header { position: absolute; left: 0; top: 30px; width: 960px; height: 100px; }
  .menu-toggle { position: absolute; left: 8px; top: 24px; width: 18px; }
  .menu-toggle span { display: block; height: 2px; background: var(--ink); margin-bottom: 4px; }
  .logo { position: absolute; left: 40px; top: 14px; font-size: 30px; font-weight: 600; color: var(--brand); letter-spacing: -0.5px; }
  .center-mark { position: absolute; left: 0; right: 0; top: 20px; text-align: center; font-family: "Questrial", sans-serif; font-size: 22px; letter-spacing: 1px; color: var(--ink); }
  .header-icons { position: absolute; right: 10px; top: 22px; display: flex; gap: 26px; }
  .main-nav { position: absolute; left: 8px; right: 8px; top: 62px; height: 36px; border-top: 1px solid var(--rule); border-bottom: 1px solid var(--rule); display: flex; justify-content: center; align-items: center; gap: 24px; font-size: 11.5px; font-weight: 500; letter-spacing: 0.6px; }

  .tile { position: absolute; }
  .photo { position: absolute; }
  .hero-photo { left: 7px; top: 138px; width: 469px; height: 417px; background: radial-gradient(circle at 50% 45%, #f6e6e0 0%, #f0d5cc 55%, #e9c6ba 100%); }
  .hero-copy { left: 484px; top: 138px; width: 469px; height: 417px; background: var(--blush); text-align: center; padding-top: 118px; }
  .hero-copy h1 { font-family: "Questrial", sans-serif; font-weight: 400; font-size: 32px; line-height: 39px; letter-spacing: 1px; }
  .hero-copy p { margin-top: 16px; font-size: 13px; line-height: 18px; color: var(--ink-soft); }
  .btn-shop { display: inline-block; margin-top: 22px; background: var(--btn); color: #fff; border-radius: 7px; width: 145px; height: 43px; line-height: 43px; font-size: 11.5px; font-weight: 500; letter-spacing: 0.6px; }

  .hand-photo { left: 7px; top: 564px; width: 469px; height: 333px; background: linear-gradient(135deg, #e9b6b5 0%, #e0a6a6 100%); }
  .bottle-photo { left: 484px; top: 564px; width: 231px; height: 333px; background: linear-gradient(180deg, #fbf0ef 0%, #f5e0de 100%); }
  .soothing { left: 723px; top: 564px; width: 230px; height: 333px; background: var(--blush-light); text-align: center; padding-top: 88px; }

  .feature { top: 906px; height: 294px; text-align: center; padding-top: 70px; }
  .feature-features { left: 7px; width: 231px; background: var(--blush-light); }
  .feature-benefits { left: 247px; width: 229px; background: var(--blush-light); }
  .feature-ingredients { left: 484px; width: 231px; background: var(--blush-mid); }
  .feature-usage { left: 723px; width: 230px; background: linear-gradient(180deg, #f0c0c1 0%, #f5cfcf 100%); }

  .icon { display: block; margin: 0 auto; }
  .tile h2 { font-family: "Jost", sans-serif; font-weight: 500; font-size: 17px; letter-spacing: 0.8px; margin-top: 20px; }
  .tile .body { font-size: 11.5px; line-height: 16px; color: var(--ink-soft); margin: 10px auto 0; width: 170px; }
  .soothing h2 { margin-top: 26px; }
</style>
</head>
<body>
  <div class="announcement">
    FREE SHIPPING ON ALL ORDERS OVER FIFTY DOLLARS
    <div class="social"><span></span><span></span><span></span></div>
  </div>

  <header class="site-header">
    <div class="menu-toggle"><span></span><span></span><span></span></div>
    <div class="logo">Lunora</div>
    <div class="center-mark">LUNORA</div>
    <div class="header-icons">
      <svg width="16" height="16" viewBox="0 0 16 16" fill="none" stroke="#231f20" stroke-width="1.5"><circle cx="8" cy="8" r="6"/><path d="M5.5 8l2 2 3-3.5"/></svg>
      <svg width="18" height="16" viewBox="0 0 18 16" fill="none" stroke="#231f20" stroke-width="1.5"><path d="M1 2h3l2 9h9l2-7H5"/><circle cx="7" cy="14" r="1"/><circle cx="14" cy="14" r="1"/></svg>
      <svg width="16" height="16" viewBox="0 0 16 16" fill="none" stroke="#231f20" stroke-width="1.5"><rect x="1.5" y="5" width="13" height="10" rx="1"/><path d="M5 5V3a3 3 0 0 1 6 0v2"/></svg>
    </div>
    <nav class="main-nav">
      <span>HOME</span><span>ABOUT</span><span>COMFORT</span><span>SCIENCE</span><span>DIRECTIONS</span><span>PRODUCTS</span><span>REVIEWS</span><span>CONTACT</span>
    </nav>
  </header>

  <div class="photo hero-photo" role="img" aria-label="Flat lay of a Lunora lotion bottle with a jar of cream, fruit slices and a small pink tube on a blush background"></div>
  <section class="tile hero-copy">
    <h1>SO GENTLE FOR<br>YOUR BODY CARE</h1>
    <p>Soothing daily moisture that helps restore natural comfort,<br>so you can feel like yourself again.</p>
    <a class="btn-shop">SHOP NOW</a>
  </section>

  <div class="photo hand-photo" role="img" aria-label="Hand holding an open jar of Lunora moisturizing cream against a pink background"></div>
  <div class="photo bottle-photo" role="img" aria-label="Lunora bottle with a peach tinted liquid and a white and pink label"></div>
  <section class="tile soothing">
    <svg class="icon" width="64" height="64" viewBox="0 0 64 64" fill="none" stroke="#231f20" stroke-width="2.5">
      <circle cx="32" cy="34" r="22"/><circle cx="32" cy="34" r="10"/>
      <path d="M32 24v20M22 34h20M25 27l14 14M39 27L25 41"/><path d="M48 18l8-8M14 50l-6 6"/>
    </svg>
    <h2>SOOTHING</h2>
    <p class="body">Gentle plant based moisture that soothes dryness and supports lasting everyday comfort.</p>
  </section>

  <section class="tile feature feature-features">
    <svg class="icon" width="72" height="72" viewBox="0 0 72 72" fill="none" stroke="#231f20" stroke-width="2.5" stroke-linejoin="round">
      <path d="M54 8l10 10-6 6-10-10z"/><path d="M50 16L18 48l-6 14 14-6 32-32"/><path d="M22 44l6 6"/>
    </svg>
    <h2>FEATURES</h2>
    <p class="body">Hormone free suppositories that melt gently for smooth and easy daily use.</p>
  </section>

  <section class="tile feature feature-benefits">
    <svg class="icon" width="72" height="72" viewBox="0 0 72 72" fill="none" stroke="#231f20" stroke-width="2.5" stroke-linecap="round">
      <path d="M10 60C26 46 42 30 62 14"/>
      <path d="M24 48c-4-6-2-12 2-14M34 38c-4-6-2-12 2-14M44 29c-3-6-1-11 3-13"/>
      <path d="M26 46c6 2 12 0 14-4M36 36c6 2 12 0 14-4M46 27c5 1 10-1 12-4"/>
    </svg>
    <h2>BENEFITS</h2>
    <p class="body">Restores natural moisture and relieves dryness so you feel comfortable again.</p>
  </section>

  <section class="tile feature feature-ingredients">
    <svg class="icon" width="72" height="72" viewBox="0 0 72 72" fill="none" stroke="#231f20" stroke-width="2.5" stroke-linejoin="round">
      <path d="M36 6l5 18 16-10-9 17 18 5-18 5 9 17-16-10-5 18-5-18-16 10 9-17-18-5 18-5-9-17 16 10z"/>
    </svg>
    <h2>INGREDIENTS</h2>
    <p class="body">Made with hyaluronic acid, vitamin E and pure organic coconut oil.</p>
  </section>

  <section class="tile feature feature-usage">
    <svg class="icon" width="72" height="72" viewBox="0 0 72 72" fill="none" stroke="#231f20" stroke-width="2.5" stroke-linejoin="round">
      <rect x="16" y="8" width="48" height="52"/><path d="M10 14v54h48"/>
      <path d="M40 46V22"/><path d="M40 34c-8-2-10-8-8-12 6 0 9 6 8 12zM40 34c8-2 10-8 8-12-6 0-9 6-8 12z"/>
    </svg>
    <h2>USAGE</h2>
    <p class="body">Insert one suppository before bed, three times a week, or as needed for comfort.</p>
  </section>
</body>
</html>
```